Modern Innovative Business Card Design

We require a nice, modern, clean business card design, ready for upload to Cardomora. Our company develops online banking software solutions for small financial insitutions. The design should be clean, professional, but yet not "corporate boring". See www.fyrolt.com for an idea of business image and profile. The design should communicate innovation, be modern and fresh, yet look professional and established.

Target Market(s)

Finance industry, bankers, entrepreneurs

Industry/Entity Type

Financial

Contact Information for Business Card

Tobias Wendlerup
CEO

FYROLT BV
Lindenwerf 38
1027 HX Amsterdam
The Netherlands

Phone: +31 20 517 8036
Direct: +31 20 604 1758
Callvo: tobias.fyrolt
ceo@fyrolt.com
www.fyrolt.com

Font styles to use
Sans Serif

Requirements
Must have
• Should look clean, modern and professional. File should be ready for upload to cardomora.
Should not have
• Boring standard corporate layout

```html
<!DOCTYPE html>
<html lang="en">
<head>
<meta charset="UTF-8">
<title>FYROLT Business Card</title>
<link rel="stylesheet" href="https://fonts.googleapis.com/css2?family=Arimo:wght@400&display=swap">
<style>
  :root {
    --backdrop: #e4e5e7;
    --card: #ffffff;
    --graphite: #5b5c5c;
    --lime: #8dc63f;
    --ink: #1a1a1a;
    --white: #ffffff;
  }
  * { margin: 0; padding: 0; box-sizing: border-box; }
  html, body {
    width: 1200px;
    height: 1200px;
    overflow: hidden;
    background: var(--backdrop);
    font-family: "Arimo", Arial, sans-serif;
  }
  .business-card {
    position: absolute;
    left: 80px;
    top: 305px;
    width: 1050px;
    height: 600px;
    background: var(--card);
  }
  .edge-bar {
    position: absolute;
    left: 0;
    top: 0;
    width: 24px;
    height: 600px;
    background: var(--graphite);
  }
  .edge-accent {
    position: absolute;
    left: 12px;
    bottom: 0;
    width: 12px;
    height: 136px;
    background: var(--lime);
    clip-path: polygon(0 8%, 100% 0, 100% 100%, 0 100%);
  }
  .wordmark {
    position: absolute;
    left: 54px;
    top: 224px;
    font-size: 98px;
    line-height: 1;
    letter-spacing: 8px;
    color: var(--graphite);
    font-weight: 400;
  }
  .company-address,
  .contact-list {
    position: absolute;
    left: 554px;
    font-size: 27px;
    line-height: 35.5px;
    color: var(--ink);
  }
  .company-address { top: 46px; }
  .contact-list { top: 380px; }
  .name-band {
    position: absolute;
    left: 554px;
    top: 217px;
    width: 496px;
    height: 114px;
    background: var(--lime);
    color: var(--white);
  }
  .person-name {
    position: absolute;
    left: 25px;
    top: 16px;
    font-size: 50px;
    line-height: 1;
    white-space: nowrap;
  }
  .person-role {
    position: absolute;
    left: 24px;
    top: 76px;
    font-size: 22px;
    letter-spacing: 2px;
    line-height: 1;
  }
</style>
</head>
<body>
  <div class="business-card">
    <div class="edge-bar"></div>
    <div class="edge-accent"></div>

    <div class="wordmark">FYROLT</div>

    <address class="company-address" style="font-style:normal">
      FYROLT BV Lindenwerf 38<br>
      1027 HX Amsterdam<br>
      The Netherlands
    </address>

    <div class="name-band">
      <div class="person-name">Tobias Wendlerup</div>
      <div class="person-role">CEO</div>
    </div>

    <div class="contact-list">
      Phone: +31 20 517 8036<br>
      Direct: +31 20 604 1758<br>
      Callvo: tobias.fyrolt<br>
      ceo@fyrolt.com<br>
      www.fyrolt.com
    </div>
  </div>
</body>
</html>
```